Business cards for the RL Group

We are looking for a template for our new business cards for our company that we can edit ourselves.
You will find our company colors in the logo. the logo on the back and on the front
first name Last Name
position
E-mail address
mobile number
landline number
Companies we have 2 RL Sicherheit GmbH and RL Services GmbH
address
Lindenbergweg 42
22459 Hamburg
www.rlgruppe-nord.de

Something modern, simple but professional

if you have any questions, bring it on.

Sicherheit

Steht in der Beschreibung

F0912C
F2A743
F7CA91
FBE8D2
FDF5EE

• recognition value
• professional
• Playful

```html
<!DOCTYPE html>
<html lang="de">
<head>
<meta charset="utf-8">
<title>RL Gruppe – Visitenkarte</title>
<link href="https://fonts.googleapis.com/css2?family=Roboto:wght@300;400;500;700&family=Roboto+Condensed:wght@700&display=swap" rel="stylesheet">
<style>
  :root {
    --orange: #f47f20;
    --charcoal: #58585a;
    --ink: #2b2b33;
    --paper: #ffffff;
    --stage-dark: #5c5b5d;
    --stage-plain: #3e3d40;
  }
  * { margin: 0; padding: 0; box-sizing: border-box; }
  html, body { width: 1200px; height: 2823px; overflow: hidden; }
  body { position: relative; background: var(--paper); font-family: "Roboto", Arial, sans-serif; }

  .stage { position: absolute; left: 0; width: 1200px; }
  .stage--orange-top { top: 0; height: 334px; background: var(--orange); }
  .stage--gray-bottom { top: 1238px; height: 459px; background: var(--stage-dark); }
  .stage--plain { top: 1701px; height: 1122px; background: var(--stage-plain); }

  .card {
    position: absolute; left: 132px; width: 951px; height: 637px;
    background: var(--paper);
    box-shadow: 18px 26px 34px rgba(0,0,0,0.45);
    overflow: hidden;
  }
  .card--first { top: 137px; }
  .card--second { top: 917px; }

  .brand {
    position: absolute; left: 34px; top: 300px; width: 340px;
    display: flex; align-items: center; gap: 16px;
  }
  .brand__square { flex: none; width: 30px; height: 30px; background: var(--orange); }
  .brand__name {
    font-family: "Roboto", Arial, sans-serif; font-weight: 700;
    font-size: 54px; line-height: 1; color: var(--charcoal); white-space: nowrap;
  }

  .contact { position: absolute; right: 69px; text-align: right; color: var(--ink); }
  .contact__name { top: 42px; font-size: 45px; font-weight: 500; color: var(--orange); line-height: 1; }
  .contact__role { top: 95px; font-size: 28px; font-weight: 300; line-height: 1; }
  .contact__phones { top: 150px; font-size: 29px; font-weight: 500; line-height: 35px; }

  .companies { position: absolute; left: 400px; top: 249px; width: 551px; height: 175px; }
  .companies svg { position: absolute; inset: 0; }
  .companies__text {
    position: absolute; right: 60px; top: 10px; text-align: right;
    font-family: "Roboto Condensed", "Arial Narrow", sans-serif; font-weight: 700;
    font-size: 33px; line-height: 40px; color: var(--ink); text-transform: uppercase;
  }
  .companies__text small { font-size: 24px; }

  .address { top: 442px; font-size: 28px; font-weight: 500; line-height: 35px; }
  .website { top: 545px; font-size: 27px; font-weight: 500; letter-spacing: 5px; }
</style>
</head>
<body>
  <div class="stage stage--orange-top"></div>
  <div class="stage stage--gray-bottom"></div>
  <div class="stage stage--plain"></div>

  <section class="card card--first" aria-label="Visitenkarte Vorderseite">
    <div class="brand"><span class="brand__square"></span><span class="brand__name">RL Gruppe</span></div>
    <p class="contact contact__name">Jonas Albrecht</p>
    <p class="contact contact__role">Managing Director</p>
    <p class="contact contact__phones">(310)555-0147<br>+98 2100555123</p>
    <div class="companies">
      <svg width="551" height="175" viewBox="0 0 551 175">
        <defs>
          <linearGradient id="wedge-a" x1="0" x2="1" y1="0" y2="0">
            <stop offset="0" stop-color="#58585a" stop-opacity="0"/>
            <stop offset="0.5" stop-color="#58585a" stop-opacity="0.8"/>
            <stop offset="1" stop-color="#58585a"/>
          </linearGradient>
        </defs>
        <polygon points="27,0 551,0 551,146 0,146" fill="#f47f20"/>
        <polygon points="10,146 551,146 551,150 30,178" fill="url(#wedge-a)"/>
      </svg>
      <p class="companies__text">Companies we have 2<br>RL Sicherheit GmbH <small>and</small><br>RL Services GmbH</p>
    </div>
    <p class="contact address">Lindenbergweg 42<br>22459 Hamburg</p>
    <p class="contact website">www.rlgruppe-nord.de</p>
  </section>

  <section class="card card--second" aria-label="Visitenkarte Rückseite">
    <div class="brand"><span class="brand__square"></span><span class="brand__name">RL Gruppe</span></div>
    <p class="contact contact__name">Jonas Albrecht</p>
    <p class="contact contact__role">Managing Director</p>
    <p class="contact contact__phones">(310)555-0147<br>+98 2100555123</p>
    <div class="companies">
      <svg width="551" height="175" viewBox="0 0 551 175">
        <defs>
          <linearGradient id="wedge-b" x1="0" x2="1" y1="0" y2="0">
            <stop offset="0" stop-color="#58585a" stop-opacity="0"/>
            <stop offset="0.5" stop-color="#58585a" stop-opacity="0.8"/>
            <stop offset="1" stop-color="#58585a"/>
          </linearGradient>
        </defs>
        <polygon points="27,0 551,0 551,146 0,146" fill="#f47f20"/>
        <polygon points="10,146 551,146 551,150 30,178" fill="url(#wedge-b)"/>
      </svg>
      <p class="companies__text">Companies we have 2<br>RL Sicherheit GmbH <small>and</small><br>RL Services GmbH</p>
    </div>
    <p class="contact address">Lindenbergweg 42<br>22459 Hamburg</p>
    <p class="contact website">www.rlgruppe-nord.de</p>
  </section>
</body>
</html>
```